依頼詳細
デザインについては、下記WEBサイトに掲載されているような
スタイリッシュかつシンプルなものが理想です。

URL: https://kinpa-morimeshi.com/contents/column/nengajyou-seisakujirei-2019/

・本来は箔押しで作成予定でしたが、納期の関係で難しいかと思っております。デザインの参考としてご確認ください。

・デザインによってはフチなし印刷の発注は可能です。

またロゴを添付しておりますが、デザイン作成に際しての
色の編集、文字部分の切り取り等は自由にしていただいて結構です。

```html
<!DOCTYPE html>
<html lang="ja">
<head>
<meta charset="utf-8">
<title>2021 Happy New Year — BRIGHT STEP INC.</title>
<link href="https://fonts.googleapis.com/css2?family=Cormorant+Garamond:wght@500;600&family=Shippori+Mincho:wght@500;600&family=Montserrat:wght@600&display=swap" rel="stylesheet">
<style>
  :root {
    --crimson: #a31f37;
    --crimson-deep: #8c1a2f;
    --crimson-shade: #6e1223;
    --gold: #e2b24a;
    --gold-soft: rgba(226, 178, 74, 0.55);
    --paper: #ffffff;
    --ink: #7a1a2c;
  }
  * { margin: 0; padding: 0; box-sizing: border-box; }
  html, body {
    width: 811px; height: 1200px; overflow: hidden;
    background: var(--paper);
  }
  .card {
    position: relative;
    width: 811px; height: 1200px;
    overflow: hidden;
    background: linear-gradient(180deg, var(--crimson) 0%, var(--crimson-deep) 100%);
  }
  .card__shapes {
    position: absolute; inset: 0;
  }
  .year {
    position: absolute;
    left: 498px; top: 238px;
    font-family: "Cormorant Garamond", serif;
    font-weight: 600;
    font-size: 60px;
    letter-spacing: 1px;
    color: var(--paper);
    text-shadow: 2px 3px 4px rgba(60, 0, 10, 0.45);
  }
  .greeting {
    position: absolute;
    left: 78px; top: 340px;
    font-family: "Cormorant Garamond", serif;
    font-weight: 500;
    font-size: 104px;
    line-height: 1;
    color: var(--paper);
    text-shadow: 3px 4px 5px rgba(60, 0, 10, 0.45);
    white-space: nowrap;
  }
  .brand {
    position: absolute;
    left: 540px; top: 1020px;
    display: flex; align-items: center; gap: 12px;
  }
  .brand__mark {
    width: 22px; height: 22px;
    background: var(--ink);
  }
  .brand__name {
    font-family: "Montserrat", sans-serif;
    font-weight: 600;
    font-size: 22px;
    letter-spacing: 1px;
    color: var(--ink);
  }
  .company {
    position: absolute;
    left: 80px; top: 1070px;
    font-family: "Shippori Mincho", serif;
    font-weight: 600;
    font-size: 21px;
    line-height: 31px;
    color: var(--ink);
    white-space: nowrap;
  }
</style>
</head>
<body>
<main class="card">
  <svg class="card__shapes" width="811" height="1200" viewBox="0 0 811 1200" aria-hidden="false">
    <defs>
      <radialGradient id="confetti-glow" cx="50%" cy="50%" r="50%">
        <stop offset="0%" stop-color="#e2b24a" stop-opacity="0.55"/>
        <stop offset="100%" stop-color="#e2b24a" stop-opacity="0"/>
      </radialGradient>
      <filter id="circle-shadow" x="-20%" y="-20%" width="140%" height="140%">
        <feDropShadow dx="6" dy="8" stdDeviation="8" flood-color="#3a0510" flood-opacity="0.45"/>
      </filter>
    </defs>

    <!-- top corner disc -->
    <circle class="corner-disc" cx="90" cy="20" r="300" fill="#9a1c33" filter="url(#circle-shadow)"/>

    <!-- gold confetti areas -->
    <ellipse role="img" aria-label="Scattered gold confetti sweeping across the top" cx="330" cy="130" rx="330" ry="95" fill="url(#confetti-glow)"/>
    <ellipse role="img" aria-label="Scattered gold confetti drifting above the white wave" cx="430" cy="860" rx="430" ry="120" fill="url(#confetti-glow)"/>

    <!-- white wave -->
    <path class="wave" d="M0 955 C 180 900, 330 1010, 520 990 C 650 975, 740 945, 811 960 L 811 1200 L 0 1200 Z" fill="#ffffff"/>
    <path class="wave-shade" d="M0 955 C 180 900, 330 1010, 520 990 C 650 975, 740 945, 811 960" fill="none" stroke="#e8d6d9" stroke-width="6"/>
  </svg>

  <div class="year">2021</div>
  <h1 class="greeting">Happy New Year</h1>

  <div class="brand">
    <span class="brand__mark"></span>
    <span class="brand__name">BRIGHT STEP INC.</span>
  </div>

  <address class="company" style="font-style:normal">
    株式会社ブライトステップ（BRIGHT STEP INC.）<br>
    〒550-0099 大阪市西区みなと町 2 丁目 3-4 さくら中央ビル 5F<br>
    TEL. 06-0000-1234　FAX. 06-0000-1235<br>
    代表者役職 代表取締役　代表者氏名 山田 太郎
  </address>
</main>
</body>
</html>
```